Roaming outings business card

please see website
www.roamingoutings.comau

info needed on card
Keiran Voss
Ph
email
Adventure Riding GPS trails

please use my logo and colours off my site

Business

Keiran Voss
keiran@roamingoutings.com

```html
<!DOCTYPE html>
<html lang="en">
<head>
<meta charset="utf-8">
<title>Roaming outings – Business card</title>
<link rel="stylesheet" href="https://fonts.googleapis.com/css2?family=Lato:wght@400;700;900&display=swap">
<style>
  :root {
    --backdrop: #e9e9eb;
    --card-white: #ffffff;
    --band-white: #f6f6f6;
    --panel-dark: #2b2c31;
    --rule-dark: #1f2024;
    --rule-soft: #55575e;
    --accent-yellow: #f7c913;
    --text-light: #ffffff;
    --text-dark: #1d1d1f;
  }
  * { margin: 0; padding: 0; box-sizing: border-box; }
  html, body {
    width: 1200px;
    height: 800px;
    overflow: hidden;
    background: var(--backdrop);
    font-family: "Lato", sans-serif;
  }
  .business-card {
    position: absolute;
    left: 150px;
    top: 130px;
    width: 900px;
    height: 540px;
    background: var(--card-white);
    overflow: hidden;
    box-shadow: 0 10px 30px rgba(0,0,0,0.18);
  }
  .name-band {
    position: absolute;
    left: 0; top: 0;
    width: 900px;
    height: 180px;
    background: var(--band-white);
  }
  .holder-name {
    position: absolute;
    left: 96px;
    top: 86px;
    font-weight: 700;
    font-size: 30px;
    letter-spacing: 0.5px;
    color: var(--text-dark);
    text-transform: uppercase;
  }
  .band-rule {
    position: absolute;
    left: 420px;
    top: 178px;
    width: 480px;
    height: 3px;
    background: var(--rule-dark);
  }
  .info-shapes {
    position: absolute;
    left: 0; top: 180px;
  }
  .contact-list {
    position: absolute;
    left: 40px;
    top: 180px;
    width: 310px;
    list-style: none;
    color: var(--text-light);
    text-align: right;
  }
  .contact-row {
    height: 86px;
    display: flex;
    flex-direction: column;
    justify-content: center;
    font-size: 20px;
    line-height: 1.3;
    border-bottom: 1px solid var(--rule-soft);
  }
  .contact-row:first-child { margin-top: 38px; }
  .contact-row:last-child { border-bottom: none; font-size: 19px; }
  .brand-lockup {
    position: absolute;
    left: 560px;
    top: 320px;
    display: flex;
    align-items: center;
    gap: 18px;
  }
  .brand-dot {
    width: 56px;
    height: 56px;
    border-radius: 50%;
    background: var(--accent-yellow);
  }
  .brand-name {
    font-weight: 900;
    font-size: 40px;
    line-height: 1;
    color: var(--text-dark);
    text-transform: uppercase;
  }
</style>
</head>
<body>
  <article class="business-card">
    <header class="name-band">
      <h1 class="holder-name">Keiran Voss</h1>
    </header>
    <div class="band-rule"></div>

    <svg class="info-shapes" width="900" height="360" viewBox="0 0 900 360" aria-hidden="true">
      <polygon points="0,0 424,0 520,360 0,360" fill="var(--panel-dark)"/>
      <polygon points="355,38 434,38 457,124 378,124" fill="var(--accent-yellow)"/>
      <polygon points="379,128 458,128 481,214 402,214" fill="var(--accent-yellow)"/>
      <polygon points="403,218 482,218 505,304 426,304" fill="var(--accent-yellow)"/>
      <g class="icon-home" fill="var(--text-light)" transform="translate(406,81)">
        <polygon points="0,-14 -16,0 -11,0 -11,12 -4,12 -4,4 4,4 4,12 11,12 11,0 16,0"/>
      </g>
      <g class="icon-phone" fill="var(--text-light)" transform="translate(430,171)">
        <path d="M-16,-4 C-16,-12 16,-12 16,-4 L16,0 L8,0 L8,-4 C8,-6 -8,-6 -8,-4 L-8,0 L-16,0 Z"/>
        <path d="M-10,2 L10,2 L14,13 L-14,13 Z"/>
      </g>
      <g class="icon-monitor" transform="translate(454,261)">
        <rect x="-15" y="-12" width="30" height="19" rx="1.5" fill="none" stroke="var(--text-light)" stroke-width="3"/>
        <rect x="-6" y="10" width="12" height="3" fill="var(--text-light)"/>
      </g>
    </svg>

    <ul class="contact-list">
      <li class="contact-row">Adventure Riding GPS trails</li>
      <li class="contact-row">408 271 653</li>
      <li class="contact-row">
        <span>keiran@roamingoutings.com</span>
        <span>www.roamingoutings.comau</span>
      </li>
    </ul>

    <div class="brand-lockup">
      <span class="brand-dot" aria-hidden="true"></span>
      <span class="brand-name">Roaming<br>outings</span>
    </div>
  </article>
</body>
</html>
```